Fashion clothing business needs a label, swing tag and business card.

Independent womenswear label called "Tessa Morwick".
I'd like a design for a woven label to go on the clothes, a swing tag and business card design. The design should be simple, modern but timeless. Its a small business, made locally in Melbourne, Australia, produces quality garments for everyday wear using beautiful fabrics.
Updates

Target Market(s)

30+ ladies, who want quality everyday wear, who don't necessarily follow trends. They can be a bit edgy and willing to take a risk with something different.

Industry/Entity Type

Clothing

Font styles to use
Other font styles liked:
• I dont mind the typewriter font, but can it look modern? happy for you to choose.

Requirements
Should not have
• A difficult shape swing tag - as it might be more expensive for me to get printed and cut.

```html
<!DOCTYPE html>
<html lang="en">
<head>
<meta charset="utf-8">
<title>Tessa Morwick — Business Card</title>
<link rel="stylesheet" href="https://fonts.googleapis.com/css2?family=Special+Elite&display=swap">
<style>
  :root {
    --card-black: #000000;
    --ink-white: #ffffff;
    --bloom-light: #f2f2f2;
    --bloom-shade: #bdbdbd;
  }
  html, body {
    margin: 0;
    padding: 0;
    width: 1200px;
    height: 734px;
    overflow: hidden;
    background: var(--card-black);
  }
  .business-card {
    position: relative;
    width: 1200px;
    height: 734px;
    overflow: hidden;
    background: var(--card-black);
    font-family: "Special Elite", "Courier New", monospace;
    color: var(--ink-white);
  }
  .bloom {
    position: absolute;
    border-radius: 50%;
    background: radial-gradient(circle at 50% 50%, var(--bloom-light) 0%, var(--bloom-light) 55%, var(--bloom-shade) 100%);
  }
  .bloom--leaf-left     { left: -79px;  top: 79px;  width: 294px; height: 294px; }
  .bloom--dahlia-top    { left: 299px;  top: -62px; width: 260px; height: 260px; }
  .bloom--petal-top     { left: 689px;  top: -51px; width: 192px; height: 192px; }
  .bloom--bud-right     { left: 954px;  top: 51px;  width: 56px;  height: 56px; }
  .bloom--rose-right    { left: 925px;  top: -23px; width: 430px; height: 430px; }
  .bloom--rose-left     { left: -46px;  top: 417px; width: 430px; height: 430px; }
  .bloom--dahlia-bottom { left: 531px;  top: 554px; width: 270px; height: 270px; }
  .bloom--rose-corner   { left: 948px;  top: 508px; width: 272px; height: 272px; }

  .card-text {
    position: absolute;
    left: 590px;
    transform: translateX(-50%);
    margin: 0;
    white-space: nowrap;
    line-height: 1;
    text-align: center;
  }
  .card-name    { top: 272px; font-size: 84px; font-weight: 400; }
  .card-email   { top: 402px; font-size: 38px; }
  .card-mobile  { top: 462px; font-size: 38px; }
</style>
</head>
<body>
  <main class="business-card">
    <div class="bloom bloom--leaf-left" role="img" aria-label="Line-drawn white flower with layered pointed leaves"></div>
    <div class="bloom bloom--dahlia-top" role="img" aria-label="Line-drawn white dahlia with teardrop petals"></div>
    <div class="bloom bloom--petal-top" role="img" aria-label="Small line-drawn white flower with scalloped petals"></div>
    <div class="bloom bloom--rose-right" role="img" aria-label="Large line-drawn white ruffled rose"></div>
    <div class="bloom bloom--bud-right" role="img" aria-label="Small line-drawn flower bud"></div>
    <div class="bloom bloom--rose-left" role="img" aria-label="Large line-drawn white ruffled rose"></div>
    <div class="bloom bloom--dahlia-bottom" role="img" aria-label="Line-drawn white dahlia with teardrop petals"></div>
    <div class="bloom bloom--rose-corner" role="img" aria-label="Line-drawn white rose with spiral centre"></div>

    <h1 class="card-text card-name">Tessa Morwick</h1>
    <p class="card-text card-email">email: info@tessamorwick.com</p>
    <p class="card-text card-mobile">mob: 0438215690</p>
  </main>
</body>
</html>
```